NU Staffing DL Flyer

Nu staffing needs a glossy brochure designed for an upcoming VIP event of our clients which are real estate agencies.

Background:
Nu Staffing specialises in Realestate recruitment in Australia. We have been in the Realestate Recruitment industry for 18 years and are the highest referred agency in the Brisbane Market. We Recruit Property Managers, Commercial and Residential, Sales and support staff for our clients.

Guideline:
- The flyer will be DL size (210x99mm)
- We would like to see designs that use the colors Green and Black same as our logo (attached)
- We would like something modern with a sleek corporate feel
- Need to include other information as detailed below in the "Must have" section
Updates

My logo and contact details is a must on the DHL flyer

Design is up to you

Kind Regards

Martin

Reason: Hi Designers Thank you for your help it is a very hard decision that is why I have made 1. prize $160 and 2. prize $100 and extended the deadline until Wednesday. Kind Regards Martin

Target Market(s)

Residential and Commercial Realestate firms in Australia

Industry/Entity Type

Real Estate

Requirements
Must have
• Why clients use NU:
With extensive years of recruitment experience we are the highest referred recruitment company in the Brisbane market.“Our clients benefit from our wealth of experience and knowledge within their industry to recruit the right candidate.”

- Why Candidates use NU:
“With our long standing experience within recruitment , we take the time and care attitude to find the right position and culture suityour working experience."

- Nu Logo
- Website details: www.nustaffing-example.com.au
- Contact details:
Martin Holroyd
Recruitment Manager
Mb: 0412 586 230
Ph: 3951 2407
Fax: 3951 2409
E: martin@nustaffing-example.com.au
Level 1/ 218 Wexcombe Street, Spring Hill QLD 4004
Nice to have
• - Why Nu does quality and background checks on candidates
- The advantage of using Nu Staffing vs Recruitment on your own
- 12 week Guarantee period on all placements

```html
<!DOCTYPE html>
<html lang="en">
<head>
<meta charset="utf-8">
<title>NU Staffing DL Flyer</title>
<link rel="stylesheet" href="https://fonts.googleapis.com/css2?family=Arimo:wght@400;700&family=Libre+Franklin:wght@700;800&display=swap">
<style>
:root{
  --green:#62bd48;
  --black:#111111;
  --white:#ffffff;
  --board:#ffffff;
  --label:#e4e4e4;
  --shadow:rgba(0,0,0,.35);
}
*{margin:0;padding:0;box-sizing:border-box}
html,body{width:1200px;height:900px;overflow:hidden;background:var(--board)}
.board{position:relative;width:1200px;height:900px;font-family:"Arimo",Arial,sans-serif}
.spec-label{position:absolute;top:0;width:101px;height:173px;background:var(--label);
  font-family:"Arimo",Arial,sans-serif;font-size:11px;color:var(--black);padding:28px 16px 0 0;text-align:right;line-height:1.3}
.spec-label strong{display:block;font-size:12px;margin-bottom:20px}
.spec-label p{margin-bottom:12px}
.spec-label--front{left:20px}
.spec-label--back{left:1080px;text-align:left;padding:28px 0 0 13px}
.panel{position:absolute;top:31px;width:394px;height:835px;box-shadow:6px 7px 6px var(--shadow);overflow:hidden}
.panel--front{left:176px;background:var(--white)}
.panel--back{left:638px;background:var(--green)}
.panel svg.shape{position:absolute;left:0;width:394px}
.wordmark{position:absolute;display:flex;align-items:center;justify-content:center;
  font-family:"Libre Franklin",Arial,sans-serif;font-weight:800;left:0;width:394px}
.wordmark .dot{border-radius:50%;background:var(--green);flex:none}
.wordmark--front{top:320px;gap:14px;font-size:44px;color:var(--green)}
.wordmark--front .dot{width:46px;height:46px}
.wordmark--back{top:770px;gap:8px;font-size:21px;color:var(--black)}
.wordmark--back .dot{width:22px;height:22px}
.intro{position:absolute;top:572px;left:0;width:394px;text-align:center;color:var(--green);font-size:15px;line-height:20.5px}
.pillars{position:absolute;top:674px;left:120px;list-style:none;font-family:"Libre Franklin",Arial,sans-serif;font-weight:700;font-size:20px;line-height:29.5px;color:var(--black)}
.pillars li::before{content:">";color:var(--green);margin-right:8px}
.reasons{position:absolute;top:46px;left:0;width:394px;text-align:center;color:var(--white)}
.reasons h2{font-family:"Libre Franklin",Arial,sans-serif;font-weight:700;font-size:15px;color:var(--black);margin-bottom:4px;letter-spacing:.2px}
.reasons p{font-size:12.4px;line-height:17.5px;margin-bottom:17px;padding:0 20px}
.call{position:absolute;top:372px;left:0;width:394px;text-align:center;font-family:"Libre Franklin",Arial,sans-serif;font-weight:700;font-size:18.5px;line-height:26px;color:var(--black)}
.call span{color:var(--white)}
.contact{position:absolute;top:449px;left:0;width:394px;text-align:center;color:var(--white);font-size:12.5px;line-height:18.2px;font-style:normal}
.contact .web{color:var(--black)}
</style>
</head>
<body>
<main class="board">
  <aside class="spec-label spec-label--front">
    <strong>FRONT</strong>
    <p>210x99mm</p>
    <p>4 process colours 2 sides</p>
  </aside>
  <aside class="spec-label spec-label--back"><strong>BACK</strong></aside>

  <section class="panel panel--front">
    <svg class="shape" style="top:0" height="200" viewBox="0 0 394 200" aria-hidden="true">
      <polygon points="0,0 394,0 196,196" fill="var(--green)"/>
    </svg>
    <div class="wordmark wordmark--front"><span class="dot"></span>NU Staffing</div>
    <p class="intro">NU Staffing Managers have<br>no higher priority than to respond<br>quickly to your needs and provide<br>you with suitable candidates.</p>
    <ul class="pillars">
      <li>OWNERSHIP</li>
      <li>EXPERIENCE</li>
      <li>ADVICE</li>
    </ul>
  </section>

  <section class="panel panel--back">
    <svg class="shape" style="bottom:0" height="200" viewBox="0 0 394 200" aria-hidden="true">
      <polygon points="0,200 394,200 196,4" fill="var(--white)"/>
    </svg>
    <div class="reasons">
      <h2>OWNERSHIP</h2>
      <p>We do quality and background checks on candidates, in addition to providing a 12 week guarantee period on all placements.</p>
      <h2>EXPERIENCE</h2>
      <p>With extensive years of recruitment experience we are the highest referred recruitment company in the Brisbane market. We take the time and care to find the right position and culture to suit the candidate's working experience.</p>
      <h2>ADVICE</h2>
      <p>Clients benefit from our wealth of experience and knowledge within the clients' industry in order to recruit the right candidate.</p>
    </div>
    <p class="call"><span>&gt;</span> Contact NU now to discuss<br>all your recruiting needs</p>
    <address class="contact">
      Martin Holroyd<br>
      Recruitment Manager<br>
      Mob: 0412 586 230<br>
      Tel: (07) 3951 2407<br>
      Fax: (07) 3951 2409<br>
      E: martin@nustaffing-example.com.au<br>
      Level 1/218 Wexcombe Street,<br>
      Spring Hill QLD 4004<br>
      <span class="web">www.nustaffing-example.com.au</span>
    </address>
    <div class="wordmark wordmark--back"><span class="dot"></span>NU Staffing</div>
  </section>
</main>
</body>
</html>
```